Billboard Design for Harbor Lane Dentistry

Brookhaven Family Dental Care
Phone number: 318-562-0913
Address: 248 Castleford Blvd
Hours: 7am-5pm ; Monday-Friday

Dental Implant Surgery
Same Day Emergency Visits
Cosmetic Treatments
GLINT! Whitening

NAMES: Dr. Colin Varnstaad
Dr. Peter Ashdale

MOST INSURANCES ACCEPTED

Eye catching slogan/colors/design for billboard

Our website is www.brookhavenfamilydentalcare.example to see current branding.

Target Market(s)

Target market is anyone in Alexandria. Focus on Families and High End Cosmetic Dentistry.

Industry/Entity Type

Dental Clinic

Requirements
Must have
• Brookhaven Family Dental Care
• Phone number: 318-562-0913
• Address: 248 Castleford Blvd
• Hours: 7am-5pm ; Monday-Friday
• Dental Implant Surgery
• Same Day Emergency Visits
• Cosmetic Treatments
• GLINT! Whitening
• NAMES: Dr. Colin Varnstaad
• Dr. Peter Ashdale
• and logo
Nice to have
• digital billboard-try to catch attention with color or phrase
Should not have
• Can not make claims or compare to other area dentist's according to laws.

```html
<!DOCTYPE html>
<html lang="en">
<head>
<meta charset="utf-8">
<title>Brookhaven Family Dental Care – Billboard</title>
<link rel="stylesheet" href="https://fonts.googleapis.com/css2?family=Montserrat:wght@500;600&family=Roboto:wght@400&family=Roboto+Condensed:wght@400;500;700&display=swap">
<style>
  :root {
    --brand-blue: #1f6db6;
    --brand-blue-edge: #2f84cb;
    --accent-sky: #6fcbe6;
    --accent-teal: #5ec3dc;
    --tagline-grey: #a9bdd2;
    --text-white: #ffffff;
    --insurance-grey: #8c8c8c;
    --paper: #ffffff;
    --photo-light: #f5f3f1;
    --photo-warm: #ecdccb;
    --photo-cool: #e2e9f1;
  }
  * { margin: 0; padding: 0; box-sizing: border-box; }
  html, body { width: 1200px; height: 571px; overflow: hidden; background: var(--paper); }

  .billboard {
    position: relative;
    width: 1200px;
    height: 571px;
    overflow: hidden;
    background: var(--paper);
    font-family: "Roboto Condensed", "Arial Narrow", sans-serif;
  }

  .family-photo {
    position: absolute;
    left: 640px; top: 0;
    width: 560px; height: 386px;
    background: linear-gradient(160deg, var(--photo-light) 0%, var(--photo-warm) 55%, var(--photo-cool) 100%);
  }

  .teal-band {
    position: absolute;
    left: 640px; top: 386px;
    width: 560px; height: 42px;
    background: var(--accent-teal);
    display: flex;
    align-items: center;
    justify-content: space-between;
    padding: 0 64px 0 52px;
    color: var(--text-white);
    font-size: 19px;
    font-weight: 500;
    letter-spacing: 0.4px;
  }

  .blue-panel {
    position: absolute;
    left: 0; top: 0;
    width: 700px; height: 571px;
  }

  .brand {
    position: absolute;
    left: 88px; top: 40px;
    width: 428px;
    text-align: center;
  }
  .brand-dot {
    display: block;
    width: 64px; height: 64px;
    margin: 0 auto 28px;
    border-radius: 50%;
    background: var(--accent-sky);
  }
  .brand-name {
    font-family: "Montserrat", sans-serif;
    font-weight: 600;
    font-size: 55px;
    line-height: 1;
    letter-spacing: 1px;
    color: var(--accent-sky);
  }
  .brand-tagline {
    margin-top: 10px;
    font-family: "Montserrat", sans-serif;
    font-weight: 500;
    font-size: 18px;
    letter-spacing: 6.4px;
    color: var(--tagline-grey);
  }

  .services {
    position: absolute;
    left: 89px; top: 246px;
    list-style: none;
  }
  .service {
    display: flex;
    align-items: center;
    height: 42px;
    color: var(--text-white);
    font-size: 22px;
    font-weight: 400;
    letter-spacing: 0.3px;
  }
  .service svg { width: 42px; height: 38px; margin-right: 16px; flex: none; }

  .hours {
    position: absolute;
    left: 89px; top: 436px;
    font-size: 32px;
    color: var(--accent-sky);
    font-weight: 400;
  }
  .phone {
    position: absolute;
    left: 89px; top: 478px;
    display: flex;
    align-items: center;
    color: var(--text-white);
    font-size: 52px;
    font-weight: 700;
    letter-spacing: 3px;
  }
  .phone svg { width: 46px; height: 46px; margin-right: 14px; }

  .insurance-note {
    position: absolute;
    right: 61px; top: 446px;
    text-align: right;
    color: var(--insurance-grey);
    font-family: "Roboto", Arial, sans-serif;
    font-size: 38px;
    line-height: 1.08;
    font-weight: 400;
  }
</style>
</head>
<body>
<div class="billboard">
  <div class="family-photo" role="img" aria-label="Photo of a smiling mother hugged from behind by her young daughter"></div>
  <div class="teal-band">
    <span class="address">248 Castleford Blvd</span>
    <span class="doctors">Dr. Colin Varnstaad &nbsp;|&nbsp; Dr. Peter Ashdale</span>
  </div>

  <svg class="blue-panel" viewBox="0 0 700 571" aria-hidden="true">
    <polygon points="0,0 612,0 684,571 0,571" fill="var(--brand-blue-edge)"/>
    <polygon points="0,0 600,0 672,571 0,571" fill="var(--brand-blue)"/>
  </svg>

  <div class="brand">
    <span class="brand-dot"></span>
    <div class="brand-name">BROOKHAVEN</div>
    <div class="brand-tagline">FAMILY DENTAL CARE</div>
  </div>

  <ul class="services">
    <li class="service">
      <svg viewBox="0 0 42 38"><rect x="2" y="8" width="28" height="28" fill="none" stroke="#6fcbe6" stroke-width="2.5"/><path d="M8 21 l7 8 L38 3" fill="none" stroke="#6fcbe6" stroke-width="4" stroke-linecap="round"/></svg>
      DENTAL IMPLANT SURGERY
    </li>
    <li class="service">
      <svg viewBox="0 0 42 38"><rect x="2" y="8" width="28" height="28" fill="none" stroke="#6fcbe6" stroke-width="2.5"/><path d="M8 21 l7 8 L38 3" fill="none" stroke="#6fcbe6" stroke-width="4" stroke-linecap="round"/></svg>
      SAME DAY EMERGENCY VISITS
    </li>
    <li class="service">
      <svg viewBox="0 0 42 38"><rect x="2" y="8" width="28" height="28" fill="none" stroke="#6fcbe6" stroke-width="2.5"/><path d="M8 21 l7 8 L38 3" fill="none" stroke="#6fcbe6" stroke-width="4" stroke-linecap="round"/></svg>
      COSMETIC TREATMENTS
    </li>
    <li class="service">
      <svg viewBox="0 0 42 38"><rect x="2" y="8" width="28" height="28" fill="none" stroke="#6fcbe6" stroke-width="2.5"/><path d="M8 21 l7 8 L38 3" fill="none" stroke="#6fcbe6" stroke-width="4" stroke-linecap="round"/></svg>
      GLINT! WHITENING
    </li>
  </ul>

  <div class="hours">7am - 5pm, Mon- Fri</div>
  <div class="phone">
    <svg viewBox="0 0 24 24"><path fill="#ffffff" d="M6.6 10.8c1.4 2.8 3.8 5.1 6.6 6.6l2.2-2.2c.3-.3.7-.4 1-.2 1.1.4 2.3.6 3.6.6.6 0 1 .4 1 1V20c0 .6-.4 1-1 1C10.6 21 3 13.4 3 4c0-.6.4-1 1-1h3.5c.6 0 1 .4 1 1 0 1.3.2 2.5.6 3.6.1.3 0 .7-.2 1z"/><path d="M15 3.5a6 6 0 0 1 5.5 5.5M15 6.8a2.8 2.8 0 0 1 2.2 2.2" fill="none" stroke="#ffffff" stroke-width="1.6" stroke-linecap="round"/></svg>
    318-562-0913
  </div>

  <div class="insurance-note">MOST INSURANCES<br>ACCEPTED</div>
</div>
</body>
</html>
```